Business Card Design - Property Management & Real Estate Services

I need a business card design for my company that I can print Pell Prints. The company is called Tarrow Management Company. It is a property management and real estate company. The design has to be clean and modern. I need two versions. One for my employee and one for me. However, the design will be the same, just different text. You can get a feel for the company by looking at our website at www.tarrowmanagement.example.

Industry/Entity Type

Property Management

Contact Information for Business Card

I will be using Pell.com to print my cards. I will most likely use the rounded edges card. I need two versions, however, they will be the same design. I need one for me and my employee.

Colors
3276b5
33a6d7

Requirements
Must have
• Company Logo
• Name of person
• Property Management & Real Estate Service
• Phone
• Email
• Website
• Address
• A space to place a QR code

```html
<!DOCTYPE html>
<html lang="en">
<head>
<meta charset="utf-8">
<title>Tarrow Management – Business Card</title>
<link rel="stylesheet" href="https://fonts.googleapis.com/css2?family=Montserrat:wght@400;500;600&family=Oswald:wght@600&display=swap">
<style>
  :root {
    --backdrop: #dcdcdc;
    --paper: #ffffff;
    --brand-blue: #1a56a0;
    --brand-mid: #3276b5;
    --brand-soft: #6fa0d2;
    --brand-pale: #d6e6f6;
    --ink-white: #ffffff;
  }
  * { box-sizing: border-box; margin: 0; padding: 0; }
  html, body { width: 1200px; height: 800px; overflow: hidden; }
  body {
    background: var(--backdrop);
    font-family: "Montserrat", sans-serif;
    display: flex;
    align-items: center;
    justify-content: center;
    gap: 48px;
  }
  .card {
    width: 525px;
    height: 300px;
    border-radius: 22px;
    overflow: hidden;
    position: relative;
    box-shadow: 0 10px 26px rgba(0,0,0,0.18);
  }

  /* Front */
  .card-front { background: var(--paper); }
  .front-brand {
    position: absolute;
    top: 0; left: 0; right: 0;
    height: 150px;
    display: flex;
    align-items: center;
    justify-content: center;
  }
  .brand-name {
    color: var(--brand-blue);
    font-weight: 500;
    text-transform: uppercase;
    text-align: center;
    line-height: 1.1;
  }
  .front-brand .brand-name { font-size: 36px; letter-spacing: 3px; }
  .brand-name small {
    display: block;
    font-size: 0.34em;
    letter-spacing: 0.9em;
    margin-top: 6px;
  }
  .band-rule {
    position: absolute;
    top: 152px; left: 0; right: 0;
    height: 2px;
    background: var(--brand-mid);
  }
  .band {
    position: absolute;
    top: 158px; left: 0; right: 0; bottom: 0;
    background: var(--brand-blue);
    color: var(--ink-white);
    display: flex;
    align-items: center;
    padding: 0 28px;
  }
  .person { flex: 0 0 205px; }
  .person-name {
    font-family: "Oswald", sans-serif;
    font-weight: 600;
    font-size: 28px;
    letter-spacing: 0.5px;
    text-transform: uppercase;
    line-height: 1.1;
  }
  .person-role { font-size: 12px; line-height: 1.4; margin-top: 4px; }
  .divider {
    width: 1px;
    align-self: stretch;
    margin: 22px 22px;
    background: rgba(255,255,255,0.6);
  }
  .contacts { list-style: none; font-size: 11px; line-height: 1.45; }
  .contacts li { display: flex; align-items: flex-start; gap: 8px; }
  .contacts li + li { margin-top: 3px; }
  .contacts svg { width: 11px; height: 11px; flex: 0 0 11px; margin-top: 2px; fill: var(--ink-white); }

  /* Back */
  .card-back {
    background: var(--brand-soft);
    display: flex;
    align-items: center;
    justify-content: center;
  }
  .card-back .brand-name {
    color: var(--brand-pale);
    font-size: 46px;
    letter-spacing: 4px;
  }
</style>
</head>
<body>

  <section class="card card-front" aria-label="Card front">
    <div class="front-brand">
      <div class="brand-name">Tarrow<small>Management</small></div>
    </div>
    <div class="band-rule"></div>
    <div class="band">
      <div class="person">
        <h1 class="person-name">Daniel Reyes</h1>
        <p class="person-role">Property Management<br>Real Estate Service</p>
      </div>
      <div class="divider"></div>
      <ul class="contacts">
        <li>
          <svg viewBox="0 0 12 12"><path d="M6 0a4 4 0 0 0-4 4c0 3 4 8 4 8s4-5 4-8a4 4 0 0 0-4-4zm0 5.6A1.6 1.6 0 1 1 6 2.4a1.6 1.6 0 0 1 0 3.2z"/></svg>
          <span>480 Harbor View Ave #210<br>Coralton, FL 33000</span>
        </li>
        <li>
          <svg viewBox="0 0 12 12"><path d="M2.4 0.6l2 2.2-1 1.4a7 7 0 0 0 4.4 4.4l1.4-1 2.2 2-1 1.8C5 11.2 0.8 7 0.6 1.6z"/></svg>
          <span>(555) 014-2280</span>
        </li>
        <li>
          <svg viewBox="0 0 12 12"><path d="M0 2h12v8H0zM0.8 2.6L6 6.6l5.2-4" stroke="#1a56a0" stroke-width="0.9"/></svg>
          <span>info@tarrowmanagement.example</span>
        </li>
        <li>
          <svg viewBox="0 0 12 12"><circle cx="6" cy="6" r="5.4" fill="none" stroke="#fff" stroke-width="1.2"/><path d="M0.8 6h10.4M6 0.6c-2.6 3-2.6 7.8 0 10.8M6 0.6c2.6 3 2.6 7.8 0 10.8" fill="none" stroke="#fff" stroke-width="1"/></svg>
          <span>www.tarrowmanagement.example</span>
        </li>
      </ul>
    </div>
  </section>

  <section class="card card-back" aria-label="Card back">
    <div class="brand-name">Tarrow<small>Management</small></div>
  </section>

</body>
</html>
```